Detox Poster Design Project

I am a naturopath that works in Melbourne. I require a poster that I can put up in my natural therapies clinic that is advertising a detox program that I am offering. The program runs for 3 or 6 weeks and is designed to help your liver, gut and kidney cleanse toxins more efficiently, leaving you feeling energised and healthy.

I would like to see designs that are fresh, organic, clear and contemporary to look at. I want to sell the idea of feeling good, wellbeing and vitality to the potential client. Colours I like include greens, greys and blues.

The final design should communicate health and happiness.

• Please include the photo of the woman in nature.Poster size will be A2 594mm by 420mm
• I have attached the design work for my business cards that you can use. It would be great if the colours and style are in keeping with the existing design work for my business. I have also attached an extra image (almond milk photo) just in case you could see a use for it.

Many thanks.
• No hippy, new age looking design.

```html
<!DOCTYPE html>
<html lang="en">
<head>
<meta charset="utf-8">
<title>It's Sensible Detox Time</title>
<link rel="stylesheet" href="https://fonts.googleapis.com/css2?family=Antonio:wght@700&family=Mulish:wght@700;800;900&display=swap">
<style>
  :root {
    --bg-blue: #4650f8;
    --bg-teal: #4a8fb0;
    --bg-green: #4dbd68;
    --title-green: #4fc46d;
    --title-edge: #d8f3df;
    --headline-white: #ffffff;
    --headline-shadow: rgba(20, 30, 60, 0.75);
    --contact-dark: #2e3438;
    --contact-glow: rgba(255, 255, 255, 0.55);
    --photo-sky: rgba(150, 190, 200, 0.45);
    --photo-figure: rgba(215, 230, 220, 0.55);
    --photo-ground: rgba(120, 185, 140, 0.45);
  }
  html, body {
    margin: 0;
    padding: 0;
    overflow: hidden;
    background: #ffffff;
  }
  .poster {
    position: relative;
    width: 1200px;
    height: 849px;
    overflow: hidden;
    background: linear-gradient(152deg, var(--bg-blue) 0%, var(--bg-teal) 45%, var(--bg-green) 85%);
    font-family: "Mulish", "Century Gothic", sans-serif;
  }
  .hero-photo {
    position: absolute;
    left: 300px;
    top: 290px;
    width: 580px;
    height: 559px;
    background:
      radial-gradient(ellipse 22% 60% at 50% 78%, var(--photo-figure), transparent 85%),
      linear-gradient(180deg, var(--photo-sky) 0%, var(--photo-ground) 100%);
    -webkit-mask-image: radial-gradient(ellipse 55% 75% at 50% 75%, #000 55%, transparent 100%);
    mask-image: radial-gradient(ellipse 55% 75% at 50% 75%, #000 55%, transparent 100%);
  }
  .title {
    position: absolute;
    top: 16px;
    left: 0;
    width: 100%;
    margin: 0;
    text-align: center;
    font-family: "Antonio", "Agency FB", sans-serif;
    font-weight: 700;
    font-size: 70px;
    line-height: 1;
    color: var(--title-green);
    -webkit-text-stroke: 1.5px var(--title-edge);
    text-shadow: 0 0 6px rgba(255, 255, 255, 0.5), 2px 3px 4px rgba(0, 0, 0, 0.25);
  }
  .headline {
    position: absolute;
    left: 0;
    width: 100%;
    margin: 0;
    text-align: center;
    font-weight: 900;
    font-size: 36px;
    line-height: 43px;
    color: var(--headline-white);
    text-shadow: 2px 2px 3px var(--headline-shadow);
  }
  .headline--question { top: 116px; }
  .headline--offer { top: 175px; }
  .headline--benefit { top: 240px; }
  .contact {
    position: absolute;
    top: 644px;
    left: 0;
    width: 100%;
    text-align: center;
    font-weight: 800;
    font-size: 31px;
    line-height: 40px;
    color: var(--contact-dark);
    text-shadow: 1px 1px 2px var(--contact-glow);
  }
  .contact p { margin: 0; }
  .contact__email-label { font-size: 31px; }
  .contact__email { font-size: 25px; }
</style>
</head>
<body>
<main class="poster">
  <div class="hero-photo" role="img" aria-label="Photo of a woman in nature seen from behind, arms raised joyfully"></div>

  <h1 class="title">It’s Sensible Detox Time</h1>

  <p class="headline headline--question">Overindulge over the holidays?</p>
  <p class="headline headline--offer">Have a detox program tailored for you.</p>
  <p class="headline headline--benefit">Press reset on your bad eating habits to feel<br>energised and vital.</p>

  <div class="contact">
    <p>For more information</p>
    <p>contact Clara Whitlow</p>
    <p>on 0400 123 456 or</p>
    <p><span class="contact__email-label">email:</span> <span class="contact__email">hello@greenleafwellness.example</span></p>
  </div>
</main>
</body>
</html>
```